Fire Protection Company

Hi we have a company called Brenlow Protection Services and are looking for a new design we are wanting flames as the last card was great with the whole background flames but you cant really see the services offered, phone, names etc.

We need something more upmarket and professional and only have a small budget

We need the words Brenlow Protection Services, Marcus Pelwey MSBuildA - Fire Safety Consultant, Phone No 0427316508 address : PO Box 8163 TRDC 4852 ABN 71264085319, HVRA Lic.5382410 Email marcus@brenlowgroup.example.com.au

Industry/Entity Type

Fire Safety

Font styles to use
Sans Serif

Colors
ec2027
ffc214

```html
<!DOCTYPE html>
<html lang="en">
<head>
<meta charset="utf-8">
<title>Brenlow Protection Services – Business Cards</title>
<link href="https://fonts.googleapis.com/css2?family=Arimo:wght@400;700&display=swap" rel="stylesheet">
<style>
  :root {
    --fire-red: #ec2027;
    --fire-red-deep: #c8141b;
    --flame-yellow: #ffc214;
    --paper: #ffffff;
    --ink: #111111;
    --backdrop: #ecebe8;
  }
  * { box-sizing: border-box; margin: 0; padding: 0; }
  html, body { width: 1200px; height: 800px; overflow: hidden; }
  body {
    background: var(--backdrop);
    font-family: "Arimo", Arial, sans-serif;
    font-weight: 700;
    position: relative;
  }
  .card {
    position: absolute;
    width: 540px;
    height: 320px;
    border-radius: 28px;
    overflow: hidden;
    box-shadow: 0 10px 28px rgba(0,0,0,0.18);
  }

  /* Services side */
  .card--services {
    left: 40px;
    top: 110px;
    background: var(--fire-red);
    color: var(--paper);
  }
  .services__flame-area {
    position: absolute;
    right: -20px;
    top: -10px;
    width: 230px;
    height: 340px;
    background: radial-gradient(ellipse at 60% 40%, var(--fire-red-deep) 0%, rgba(200,20,27,0.6) 55%, rgba(236,32,39,0) 80%);
  }
  .services__brand {
    position: absolute;
    left: 24px;
    top: 30px;
    display: flex;
    align-items: center;
    gap: 10px;
  }
  .brand-dot {
    width: 20px; height: 20px;
    border-radius: 50%;
    background: var(--flame-yellow);
    flex: none;
  }
  .brand-name--light {
    font-size: 23px;
    line-height: 1.1;
    color: var(--paper);
    width: 230px;
  }
  .services__rule {
    position: absolute;
    left: 0; right: 0;
    top: 100px;
    height: 4px;
    background: var(--paper);
  }
  .services__list {
    position: absolute;
    top: 122px;
    left: 26px;
    right: 22px;
    display: grid;
    grid-template-columns: 170px 1fr;
    column-gap: 18px;
    row-gap: 16px;
    font-size: 16px;
    line-height: 1.18;
    list-style: none;
  }

  /* Contact side */
  .card--contact {
    left: 620px;
    top: 360px;
    background: var(--paper);
    color: var(--ink);
  }
  .contact__brand {
    position: absolute;
    left: 26px;
    top: 128px;
    display: flex;
    align-items: center;
    gap: 10px;
  }
  .brand-name--red {
    font-size: 23px;
    line-height: 1.1;
    color: var(--fire-red);
    width: 170px;
  }
  .contact__divider {
    position: absolute;
    left: 228px;
    top: 40px;
    width: 4px;
    height: 248px;
    background: var(--fire-red);
  }
  .contact__details {
    position: absolute;
    left: 244px;
    top: 40px;
    right: 16px;
  }
  .contact__name {
    font-size: 20px;
    color: var(--fire-red);
    white-space: nowrap;
  }
  .contact__title {
    font-size: 15px;
    margin-top: 4px;
  }
  .contact__lines {
    list-style: none;
    margin-top: 32px;
    font-size: 14.5px;
    line-height: 1.3;
  }
  .contact__lines li {
    display: flex;
    gap: 8px;
    align-items: flex-start;
    margin-bottom: 4px;
  }
  .contact__lines li.contact__email {
    margin-top: 30px;
    font-size: 12.5px;
    white-space: nowrap;
  }
  .icon { width: 14px; height: 14px; flex: none; margin-top: 2px; fill: var(--ink); }
</style>
</head>
<body>

  <section class="card card--services" aria-label="Services side">
    <div class="services__flame-area" role="img" aria-label="Large decorative flame shapes in deep red"></div>
    <div class="services__brand">
      <span class="brand-dot"></span>
      <span class="brand-name--light">Brenlow Protection Services</span>
    </div>
    <div class="services__rule"></div>
    <ul class="services__list">
      <li>Fire Safety Adviser</li>
      <li>Sales / Service and Maintenance of Portable Fire Equipment</li>
      <li>Fire Training</li>
      <li>Hydrant Flow and Pressure Tests</li>
      <li>Fire and Evacuation Plans</li>
      <li>Smoking Alarm Inspections In Rental Properties</li>
    </ul>
  </section>

  <section class="card card--contact" aria-label="Contact side">
    <div class="contact__brand">
      <span class="brand-dot"></span>
      <span class="brand-name--red">Brenlow Protection Services</span>
    </div>
    <div class="contact__divider"></div>
    <div class="contact__details">
      <p class="contact__name">Marcus Pelwey MSBuildA</p>
      <p class="contact__title">Fire Safety Consultant</p>
      <ul class="contact__lines">
        <li>
          <svg class="icon" viewBox="0 0 24 24" aria-hidden="true"><path d="M6.6 10.8a15 15 0 0 0 6.6 6.6l2.2-2.2a1 1 0 0 1 1-.25 11.4 11.4 0 0 0 3.6.57 1 1 0 0 1 1 1V20a1 1 0 0 1-1 1A17 17 0 0 1 3 4a1 1 0 0 1 1-1h3.5a1 1 0 0 1 1 1c0 1.25.2 2.450.57 3.57a1 1 0 0 1-.25 1z"/></svg>
          <span>0427316508</span>
        </li>
        <li>
          <svg class="icon" viewBox="0 0 24 24" aria-hidden="true"><path d="M12 3 2 12h3v9h5v-6h4v6h5v-9h3z"/></svg>
          <span>PO Box 8163 TRDC 4852<br>ABN 71264085319,<br>HVRA, Lic. 5382410</span>
        </li>
        <li class="contact__email">
          <svg class="icon" viewBox="0 0 24 24" aria-hidden="true"><path d="M2 5h20v14H2zm2 2v.5l8 5 8-5V7z"/></svg>
          <span>marcus@brenlowgroup.example.com.au</span>
        </li>
      </ul>
    </div>
  </section>

</body>
</html>
```